Harbourline Metro Business Racquet Circuit (est.1952)

The Metro Business Racquet Circuit began in 1952 and has been played every year since. It is the longest running continuous sporting competition in the Sydney CBD. It is a team squash competition from May to Oct yearly played between companies, sporting groups or just a groups of friends.
We are looking for a flyer that we can reuse every year (so the content within the flyer can't be tied to a specific time). Other specific we are looking for are
1. Squash imagery (can either be real or graphic design) depicting action / athleticism / friendly rivalry
2. Needs the following content
a ) "A Sydney CBD based competition for friendly rivalry between companies, sporting clubs or between friends"
b) "All matches in and around the CBD from 5.30pm to 8pm"
c) "We cater for all playing abilities"
d) "Ladies beginner comp includes complimentary coaching"
e) "Visit our website www.plvqn.org.au for more info or contact Walter on frontw@qmx.com.au"

Flyer needs to include the logos attached in file upload section

```html
<!DOCTYPE html>
<html lang="en">
<head>
<meta charset="utf-8">
<title>Metro Business Racquet Circuit – Flyer</title>
<link rel="stylesheet" href="https://fonts.googleapis.com/css2?family=Lato:wght@700;900&family=Cabin:wght@400;600;700&display=swap">
<style>
  :root{
    --page:#ffffff;
    --blue-top:#4173b8;
    --blue-mid:#4a93d0;
    --night:#1f2020;
    --ink:#1b1b1b;
    --white:#ffffff;
    --amber:#f8bb17;
    --orange:#f6b21c;
    --lime:#cadb2f;
    --sky:#27a8e0;
    --stroke-blue:#3f6fbe;
    --red:#d9252f;
  }
  html,body{margin:0;padding:0;}
  body{
    width:1200px;height:954px;overflow:hidden;position:relative;
    background:var(--page);
    font-family:"Cabin",sans-serif;
  }
  .flyer{position:absolute;left:63px;top:85px;width:1076px;height:762px;overflow:hidden;background:var(--night);}

  .header{position:absolute;left:0;top:0;width:1076px;height:187px;
    background:linear-gradient(180deg,var(--blue-top),var(--blue-mid));}
  .headline{position:absolute;left:50px;top:25px;margin:0;
    font-family:"Lato",sans-serif;font-weight:900;font-size:73px;line-height:1;
    color:var(--white);letter-spacing:0.5px;}
  .intro{position:absolute;left:51px;top:106px;margin:0;
    font-size:27px;line-height:35px;color:var(--white);font-weight:400;}

  .brand{position:absolute;left:860px;top:52px;width:190px;height:90px;
    display:flex;align-items:center;gap:10px;}
  .brand-dot{width:22px;height:22px;border-radius:50%;background:var(--amber);flex:none;}
  .brand-name{font-family:"Cabin",sans-serif;font-weight:700;font-size:26px;line-height:1.05;color:var(--white);}

  .player{position:absolute;left:60px;top:200px;width:380px;height:490px;
    background:radial-gradient(ellipse at 45% 45%,#4b4d52 0%,#2a2b2e 55%,var(--night) 100%);}

  .ladies{position:absolute;left:637px;top:218px;margin:0;
    font-family:"Lato",sans-serif;font-weight:900;font-size:35px;line-height:1;white-space:nowrap;}
  .ladies .w1{color:var(--orange);}
  .ladies .w2{color:var(--lime);}
  .ladies .w3{color:var(--sky);}
  .coaching{position:absolute;left:637px;top:258px;margin:0;
    font-size:27px;color:var(--white);white-space:nowrap;}

  .time-panel{position:absolute;left:0;top:0;width:1076px;height:762px;}

  .matches{position:absolute;left:630px;top:354px;width:460px;margin:0;
    font-size:23px;color:var(--ink);text-align:center;}
  .time-pill{position:absolute;left:618px;top:398px;width:425px;height:71px;border-radius:36px;
    background:var(--ink);color:var(--white);
    font-family:"Lato",sans-serif;font-weight:900;font-size:52px;
    display:flex;align-items:center;justify-content:center;letter-spacing:0.5px;}
  .abilities{position:absolute;left:620px;top:476px;width:425px;margin:0;
    font-family:"Lato",sans-serif;font-weight:900;font-size:27px;color:var(--ink);
    text-align:center;white-space:nowrap;}

  .club-seal{position:absolute;left:482px;top:576px;width:86px;height:86px;border-radius:50%;
    background:radial-gradient(circle,#233469 60%,#c9a043 62%,#b8892e 100%);}

  .partners{position:absolute;left:584px;top:586px;width:492px;height:65px;background:var(--white);
    display:flex;align-items:center;gap:22px;padding-left:14px;box-sizing:border-box;}
  .partner{display:flex;align-items:center;gap:6px;font-size:13px;line-height:1.1;white-space:nowrap;}
  .partner-mark{width:14px;height:14px;border-radius:50%;flex:none;}
  .partner-academy{color:#2a8fc9;font-weight:600;}
  .partner-academy .partner-mark{background:#2a8fc9;}
  .partner-short{color:var(--red);font-weight:600;}
  .partner-short .partner-mark{background:var(--red);}
  .partner-assoc{color:var(--ink);font-weight:400;letter-spacing:0.6px;font-size:12.5px;}

  .footer{position:absolute;left:0;top:691px;width:1076px;height:71px;
    background:linear-gradient(180deg,var(--blue-mid),var(--blue-top));}
  .contact{position:absolute;left:51px;top:22px;margin:0;font-size:21px;color:var(--white);white-space:nowrap;}
  .contact strong{font-family:"Lato",sans-serif;font-weight:900;}
</style>
</head>
<body>
  <main class="flyer">
    <header class="header">
      <h1 class="headline">A Sydney CBD based</h1>
      <p class="intro">competition for friendly rivalry between companies,<br>sporting clubs or between friends</p>
      <div class="brand">
        <span class="brand-dot"></span>
        <span class="brand-name">CourtLine<br>Metro</span>
      </div>
    </header>

    <div class="player" role="img" aria-label="Photo of a female squash player lunging to hit a low forehand"></div>

    <p class="ladies"><span class="w1">Ladies</span> <span class="w2">beginner</span> <span class="w3">comp</span></p>
    <p class="coaching">includes complimentary coaching</p>

    <svg class="time-panel" viewBox="0 0 1076 762" aria-hidden="true">
      <path d="M724 329 C640 332 560 380 482 436 C560 492 640 540 724 544" fill="none" stroke="var(--stroke-blue)" stroke-width="4"/>
      <path d="M1076 329 L730 329 C650 332 585 380 505 436 C585 492 650 540 730 544 L1076 544 Z" fill="var(--amber)"/>
    </svg>

    <p class="matches">All matches in and around the CBD from</p>
    <div class="time-pill">5.30pm to 8pm</div>
    <p class="abilities">We cater for all playing abilities</p>

    <div class="club-seal" aria-hidden="true"></div>

    <div class="partners">
      <span class="partner partner-academy"><span class="partner-mark"></span>Bayside Squash<br>Academy</span>
      <span class="partner partner-short"><span class="partner-mark"></span>HTRA</span>
      <span class="partner partner-assoc">HARBOUR TOWERS RACQUET ASSOCIATION</span>
    </div>

    <footer class="footer">
      <p class="contact"><strong>Visit our website www.plvqn.org.au</strong> for more info or contact <strong>Walter on frontw@qmx.com.au</strong></p>
    </footer>
  </main>
</body>
</html>
```